Corwin Crest Homes Needs Business Card Design

Looking for a unique modern business card to fit my new Logo.
Name: Marcus Corwin
Company: Corwin Crest Homes, LLC
Tag Line: Always Built Better
Email: corwincresthomes@mailnest.example
Phone: (555) 017-2846
Website: www.corwincresthomes.example
License: CORWICH462KX

```html
<!DOCTYPE html>
<html lang="en">
<head>
<meta charset="utf-8">
<title>Corwin Crest Homes – Business Card</title>
<link href="https://fonts.googleapis.com/css2?family=Figtree:wght@400;700;800&display=swap" rel="stylesheet">
<style>
  :root {
    --page-bg: #e4e4e4;
    --card-blue: #2e90c6;
    --card-blue-light: #3da0cd;
    --card-blue-deep: #2780b8;
    --mark-blue: #226d9c;
    --card-white: #f1f1f1;
    --ink: #1c1c1c;
    --brand-blue: #2a7fb9;
    --accent-blue: #3696d0;
    --tagline: #ffffff;
  }
  html, body {
    margin: 0;
    width: 1200px;
    height: 1200px;
    overflow: hidden;
    background: var(--page-bg);
    font-family: "Figtree", Arial, sans-serif;
  }
  .canvas {
    position: relative;
    width: 1200px;
    height: 1200px;
  }
  .card {
    position: absolute;
    left: 234px;
    width: 731px;
    height: 418px;
    box-sizing: border-box;
  }
  .card-front {
    top: 160px;
    background: linear-gradient(35deg, var(--card-blue-deep), var(--card-blue) 50%, var(--card-blue-light));
  }
  .card-back {
    top: 632px;
    background: var(--card-white);
  }

  /* front */
  .front-brand {
    position: absolute;
    left: 0;
    right: 0;
    top: 128px;
    text-align: center;
    color: var(--mark-blue);
  }
  .front-brand .brand-square {
    display: block;
    width: 34px;
    height: 34px;
    margin: 0 auto 14px;
    background: var(--mark-blue);
  }
  .front-brand .brand-name {
    font-weight: 800;
    font-size: 24px;
    line-height: 1.15;
    letter-spacing: 0.5px;
  }
  .tagline {
    position: absolute;
    left: 0;
    right: 0;
    top: 355px;
    text-align: center;
    color: var(--tagline);
    font-size: 19px;
    font-weight: 400;
    letter-spacing: 0.2px;
  }

  /* back */
  .back-brand {
    position: absolute;
    left: 510px;
    width: 180px;
    top: 52px;
    text-align: center;
  }
  .back-brand .brand-square {
    display: block;
    width: 46px;
    height: 46px;
    margin: 0 auto 16px;
    background: var(--accent-blue);
  }
  .back-brand .brand-name {
    color: var(--ink);
    font-weight: 800;
    font-size: 26px;
    line-height: 1.12;
  }
  .person-name {
    position: absolute;
    left: 49px;
    top: 177px;
    margin: 0;
    color: var(--brand-blue);
    font-size: 32px;
    font-weight: 800;
    letter-spacing: -0.3px;
  }
  .company-name {
    position: absolute;
    left: 49px;
    top: 253px;
    margin: 0;
    color: var(--brand-blue);
    font-size: 21px;
    font-weight: 700;
  }
  .contact-list {
    position: absolute;
    left: 49px;
    top: 289px;
    margin: 0;
    padding: 0;
    list-style: none;
    color: var(--ink);
    font-size: 19.5px;
  }
  .contact-list li {
    display: flex;
    align-items: center;
    height: 28px;
  }
  .contact-list svg {
    width: 16px;
    height: 16px;
    margin-right: 9px;
    flex: none;
  }
  .license {
    position: absolute;
    right: 48px;
    top: 345px;
    color: var(--ink);
    font-size: 19.5px;
  }
</style>
</head>
<body>
<div class="canvas">

  <section class="card card-front">
    <div class="front-brand">
      <span class="brand-square"></span>
      <div class="brand-name">Corwin Crest<br>Homes</div>
    </div>
    <p class="tagline">Always Built Better</p>
  </section>

  <section class="card card-back">
    <div class="back-brand">
      <span class="brand-square"></span>
      <div class="brand-name">Corwin Crest<br>Homes</div>
    </div>

    <h1 class="person-name">Marcus Corwin</h1>
    <h2 class="company-name">Corwin Crest Homes, LLC</h2>

    <ul class="contact-list">
      <li>
        <svg viewBox="0 0 16 16" aria-hidden="true"><path fill="#2a7fb9" d="M3.5 1.5l2.2 2.6-1.3 1.6c.8 1.9 2.1 3.2 4 4l1.6-1.3 2.6 2.2-1.2 2.2c-.3.5-.9.7-1.5.5C5.9 12.2 3.8 10.1 2.7 6.1c-.2-.6 0-1.2.5-1.5z"/><path fill="none" stroke="#2a7fb9" stroke-width="1.2" d="M9 2.5a4.5 4.5 0 0 1 4.5 4.5M9 4.8a2.2 2.2 0 0 1 2.2 2.2"/></svg>
        (555) 017-2846
      </li>
      <li>
        <svg viewBox="0 0 16 16" aria-hidden="true"><rect x="1" y="3" width="14" height="10" rx="1" fill="#2a7fb9"/><path d="M1.5 4l6.5 5 6.5-5" fill="none" stroke="#f1f1f1" stroke-width="1.3"/></svg>
        corwincresthomes@mailnest.example
      </li>
      <li>
        <svg viewBox="0 0 16 16" aria-hidden="true"><g fill="none" stroke="#2a7fb9" stroke-width="1.4"><circle cx="8" cy="8" r="6.5"/><ellipse cx="8" cy="8" rx="2.8" ry="6.5"/><path d="M1.5 8h13"/></g></svg>
        www.corwincresthomes.example
      </li>
    </ul>

    <p class="license" style="margin:0">License: CORWICH462KX</p>
  </section>

</div>
</body>
</html>
```